Portugal:the best eco sun-dried tomato in the world needs a packaging design

We produce the best sun-dried tomatoes in the world...we know that, even that competition doesn´t exist...yet!
We are a "solar farm" in Portugal, reducing carbon footprint producing beautiful and healthy local food, with mules...the traditional way in a new way. Our tomatoes are hand-picked and sun dried, in a very "slow food" way.
The costumers for our product -we are a small farm - can only be good foodstores and airports, we'd love to export the best of Portugal elsewhere. In a glass jar of c. 250 ml, with a nice top and a nice logo+description...one that stands out of the others and conveys our eco, local, solar message.
Oh, and I forgot...our sun-dried tomatoes are packed with our beautiful olive oil..and yes, that olive oil has already won the best olive oil in the world! For sure!
I'll send photos for the interested, you'll love it; and the best olive oil and sun-dried tomatoes in the world for the winner!

Target Market(s)

nice foodstores
foodies
airport stores

Industry/Entity Type

Food Store

Font styles to use
Decorative
Script

Requirements
Must have
• Portugal
• Sun dried tomatoes
• Best olive oil in the world
• Traditional methods
• Sustainable farming
Nice to have
• a photo of our mules working...sent to interested designers

```html
<!DOCTYPE html>
<html lang="en">
<head>
<meta charset="utf-8">
<title>Sun Dried Tomatoes in Olive Oil – Jar Label</title>
<link rel="stylesheet" href="https://fonts.googleapis.com/css2?family=Playfair+Display:wght@400;500&family=Great+Vibes&family=Cormorant+Garamond:wght@500&display=swap">
<style>
  :root {
    --page: #ffffff;
    --label-ground: #f7f3f1;
    --label-accent: #efe4e1;
    --tomato-red: #d8191b;
    --cream: #fff6f2;
  }
  html, body {
    margin: 0;
    padding: 0;
    width: 1200px;
    height: 1200px;
    overflow: hidden;
    background: var(--page);
  }
  .canvas {
    position: relative;
    width: 1200px;
    height: 1200px;
  }
  .label {
    position: absolute;
    left: 60px;
    top: 142px;
    width: 1080px;
    height: 916px;
  }
  .label-pattern {
    position: absolute;
    inset: 0;
    background: radial-gradient(circle at 30% 30%, var(--label-ground) 0%, var(--label-accent) 100%);
  }
  .front-panel {
    position: absolute;
    left: 136px;
    top: 89px;
    width: 791px;
    height: 740px;
    background: var(--tomato-red);
    color: var(--cream);
    text-align: center;
    box-sizing: border-box;
  }
  .origin-line {
    position: absolute;
    top: 92px;
    left: 0;
    right: 0;
    margin: 0;
    font-family: "Great Vibes", cursive;
    font-size: 84px;
    font-weight: 400;
    line-height: 1;
  }
  .product-name {
    position: absolute;
    top: 232px;
    left: 0;
    right: 0;
    margin: 0;
    font-family: "Playfair Display", serif;
    font-weight: 400;
    font-size: 112px;
    line-height: 1.08;
    letter-spacing: -1px;
  }
  .packing-medium {
    position: absolute;
    top: 500px;
    left: 0;
    right: 0;
    margin: 0;
    font-family: "Great Vibes", cursive;
    font-size: 78px;
    line-height: 1;
  }
  .tagline {
    position: absolute;
    top: 640px;
    left: 0;
    right: 0;
    margin: 0;
    font-family: "Cormorant Garamond", serif;
    font-weight: 500;
    font-size: 21px;
    letter-spacing: 2.5px;
    text-transform: uppercase;
  }
</style>
</head>
<body>
  <main class="canvas">
    <section class="label">
      <div class="label-pattern" role="img" aria-label="Repeating hand-drawn pattern of halved tomatoes in black line art with some red filled tomatoes"></div>
      <div class="front-panel">
        <p class="origin-line">Portugal's Best</p>
        <h1 class="product-name">SUN DRIED<br>TOMATOES</h1>
        <p class="packing-medium">in Olive Oil</p>
        <p class="tagline">Sustainable Farming Product</p>
      </div>
    </section>
  </main>
</body>
</html>
```